Building company needs a letterhead design

I'm after a modern but professional letter head.
Must have the below details:
- Logo
- Website - TARVELBUILD.COM.AU
- Email - INFO@TARVELBUILD.COM.AU
- Office - 03 52631848
- Mobile number - 0413596281
- ABN - 47 318 965 102
...........................................................................................................................................................................................................................
- Logo
- Office - 03 52631848
- ABN - 47 318 965 102

Target Market(s)

.

Industry/Entity Type

Construction Company

Font styles to use
Sans Serif

Requirements
Must have
• Must have the below details:
• - Logo
• - Website - TARVELBUILD.COM.AU
• - Email - INFO@TARVELBUILD.COM.AU
• - Office - 03 52631848
• - Mobile number - 0413596281
• - ABN - 47 318 965 102
Nice to have
• .
Should not have
• .

```html
<!DOCTYPE html>
<html lang="en">
<head>
<meta charset="utf-8">
<title>Tarvel Building Group – Letterhead</title>
<link href="https://fonts.googleapis.com/css2?family=Open+Sans:wght@400;600;700&family=Barlow:wght@600;700;800&display=swap" rel="stylesheet">
<style>
  :root {
    --brand-orange: #f8b323;
    --brand-grey: #8a8b8e;
    --brand-dark: #3c3c3e;
    --ink: #2e2e30;
    --label-blue: #2c3a90;
    --paper: #ffffff;
    --crop: #555555;
  }
  html, body { margin: 0; padding: 0; overflow: hidden; background: var(--paper); }
  .sheet {
    position: relative;
    width: 883px;
    height: 1200px;
    overflow: hidden;
    background: var(--paper);
    font-family: "Open Sans", Arial, sans-serif;
    color: var(--ink);
  }
  .crop-marks { position: absolute; inset: 0; pointer-events: none; }

  .brand {
    position: absolute;
    left: 116px;
    top: 92px;
    display: flex;
    align-items: center;
    gap: 12px;
  }
  .brand-square {
    width: 52px; height: 52px;
    background: var(--brand-orange);
  }
  .brand-name {
    font-family: "Barlow", Arial, sans-serif;
    font-weight: 800;
    font-size: 25px;
    line-height: 1.05;
    letter-spacing: 0.5px;
    color: var(--brand-orange);
  }

  .contact {
    position: absolute;
    right: 98px;
    top: 110px;
    text-align: right;
    font-size: 9.5px;
    line-height: 12.5px;
    color: var(--brand-dark);
  }
  .contact .label { color: var(--label-blue); }

  .recipient {
    position: absolute;
    left: 163px;
    top: 304px;
    font-size: 15.5px;
    line-height: 20.5px;
  }
  .recipient .recipient-name {
    font-family: "Barlow", Arial, sans-serif;
    font-weight: 700;
  }

  .letter-body {
    position: absolute;
    left: 163px;
    top: 446px;
    width: 563px;
    font-size: 15.3px;
    line-height: 20.8px;
    text-align: justify;
  }
  .letter-body p { margin: 0 0 20.8px; }

  .signature {
    position: absolute;
    left: 163px;
    top: 907px;
    font-size: 15.5px;
    line-height: 20.5px;
  }

  .footer { position: absolute; left: 0; top: 1160px; width: 883px; height: 40px; }
  .footer-web {
    position: absolute;
    left: 676px;
    top: 1165px;
    font-size: 10px;
    line-height: 30px;
    color: var(--paper);
  }
</style>
</head>
<body>
<div class="sheet">
  <svg class="crop-marks" width="883" height="1200" viewBox="0 0 883 1200">
    <g stroke="var(--crop)" stroke-width="1">
      <line x1="36" y1="6" x2="36" y2="28"/><line x1="6" y1="36" x2="28" y2="36"/>
      <line x1="847" y1="6" x2="847" y2="28"/><line x1="855" y1="36" x2="877" y2="36"/>
      <line x1="36" y1="1172" x2="36" y2="1194"/><line x1="6" y1="1164" x2="28" y2="1164"/>
      <line x1="847" y1="1172" x2="847" y2="1194"/><line x1="855" y1="1164" x2="877" y2="1164"/>
    </g>
  </svg>

  <div class="brand">
    <div class="brand-square"></div>
    <div class="brand-name">TARVEL<br>BUILDING GROUP</div>
  </div>

  <div class="contact">
    <div>47 318 965 102 <span class="label">ABN</span></div>
    <div>INFO@TARVELBUILD.COM.AU</div>
    <div><span class="label">Ph</span> 03 52631848 &nbsp;0413 596 281 <span class="label">Mob</span></div>
  </div>

  <div class="recipient">
    <div class="recipient-name">Mr. Daniel Harrow</div>
    <div>Managing Director</div>
    <div>SYDNEY Investor</div>
    <div>52 Kerr Street</div>
    <div>AU</div>
  </div>

  <div class="letter-body">
    <p>Lorem Ipsum is simply dummy text for printing and typesetting industry. Lorem Ipsum has been the industry’s standard dummy text since the 1500s, when an unknown printer galley of type and scrambled it to make a type specimen book. It has suvived not only manual but also the leap into electronic typesetting, remaining essentially un changed. It was popularised in the 1960s with the release of Presstype sheets containing Lorem Ipsum pass and more recently with desktop publishing software like PageForm Studio including version 6.9 of Lorem Ipsum.</p>
    <p>Country to popular belief, Lorem Ipsum is not simply random text. It has roots in a piece of sical Latin literature from 45 BC, making it over 2000 years old. Oliver Brandt, a prfessor at Larkfield College in Vermont, looked up one of the most of the world classical literature, discovered the undoubtable sorce. Lorem Ipsum comes from section 1.10.32 and 1.10.33 of “de Finibus Bonorum et Molorum” ( The Extreme of Good and Even Cicero), written in 45 BC. This book is a treatise on the theory of ethics very popular during Renassiance.</p>
    <p>Thank you for being one of our valued customers.</p>
  </div>

  <div class="signature">
    <div>Name Here</div>
    <div>CEO</div>
  </div>

  <svg class="footer" width="883" height="40" viewBox="0 0 883 40">
    <polygon points="24,6 596,6 578,36 24,36" fill="var(--brand-grey)"/>
    <polygon points="604,0 858,0 858,36 581,36" fill="var(--brand-orange)"/>
  </svg>
  <div class="footer-web">TARVELBUILD.COM.AU</div>
</div>
</body>
</html>
```